FINANCIAL MANAGEMENT COMPANY LOGO

LOGO, BUSINESS CARD & STATIONERY

NEW FINANCIAL MANAGEMENT COMPANY

name: ORVEL Financial Management Pty Ltd
abn xx xxx xxx xxx
address: (not yet available)
Telephone: (not yet available)

Strategic Financial Planning and Management Company

- Superannuation
- SMSF (Own Fund)
- Retail/Industry Funds (fund controlled)

- Personal Wealth
- Planning
- Forcasting
- Portfolio Management

- Future Generations
- Strategy
- Structural Implimenation and Management

- Risk Insurance
- Analysis
- Implimentation
- Review

NOTES:
I would like to project professionalism, security and personal care.
Comforting, warm colours

Name on Business card:

Maren Toll
FPRB Authorised Financial Strategist

THANK YOU FOR THE SUBMISSIONS .......
I WOULD LIKE TO SEE EARTHY AND  RELAXED TONES WITH AN UNDERSTANDING OF AN 'ALL INCLUSIVE  & CARING' FEEL.
REALLY APPRECIATE ALL THE  IDEAS SO FAR....

Target Market(s)

Middle aged, reasonably wealthy, successful,

Industry/Entity Type

Security

Logo Text

ORVEL Financial Management Pty Ltd

Logo styles of interest
Abstract Logo
Requirements
Must have
• business card to carry full deatils of company and it's services (as previously described in this brief)
Nice to have
• Logo to be easily recognised on all stationey and advertising boards

```html
<!DOCTYPE html>
<html lang="en">
<head>
<meta charset="utf-8">
<title>ORVEL Financial Management – Business Card</title>
<link rel="stylesheet" href="https://fonts.googleapis.com/css2?family=Questrial&family=Arimo:wght@400&display=swap">
<style>
  :root {
    --ink: #0d0d0d;
    --paper: #ffffff;
    --olive-dark: #6c6b58;
    --olive-mid: #9a9884;
    --stone-light: #e6e4dd;
    --stone-pale: #f4f3ef;
    --mark-dark: #111314;
    --mark-slate: #7e8b8c;
  }
  * { margin: 0; padding: 0; box-sizing: border-box; }
  html, body {
    width: 1200px; height: 687px; overflow: hidden;
    background: var(--paper);
  }
  .card {
    position: relative;
    width: 1200px; height: 687px;
    border: 4px solid var(--ink);
    background: var(--paper);
    overflow: hidden;
    font-family: "Questrial", sans-serif;
    color: var(--ink);
  }
  .header-left {
    position: absolute; left: 0; top: 62px; width: 287px; height: 157px;
    background: linear-gradient(180deg, var(--paper) 0%, var(--stone-light) 100%);
  }
  .header-band {
    position: absolute; left: 287px; top: 62px; right: 0; height: 157px;
    background: linear-gradient(180deg, var(--olive-dark) 0%, var(--olive-mid) 70%, #b3b1a0 100%);
  }
  .divider {
    position: absolute; left: 0; right: 0; top: 217px; height: 3px;
    background: var(--ink);
  }
  .side-column {
    position: absolute; left: 0; top: 220px; width: 287px; bottom: 0;
    background: linear-gradient(180deg, var(--stone-light) 0%, #a8a690 100%);
  }
  .content-panel {
    position: absolute; left: 287px; top: 220px; right: 0; bottom: 0;
    background: linear-gradient(200deg, var(--olive-mid) 0%, #c2c0b1 40%, var(--stone-pale) 100%);
  }
  .brand-name {
    position: absolute; left: 10px; top: 38px;
    font-size: 150px; line-height: 1; letter-spacing: 2px;
    font-weight: 400;
  }
  .brand-descriptor {
    position: absolute; left: 560px; top: 166px;
    font-size: 40px; line-height: 1;
  }
  .mark-area {
    position: absolute; left: 12px; top: 279px; width: 255px; height: 348px;
  }
  .holder-name {
    position: absolute; left: 307px; top: 302px;
    font-family: "Arimo", sans-serif; font-size: 41px; line-height: 1;
  }
  .holder-title {
    position: absolute; left: 309px; top: 354px;
    font-family: "Arimo", sans-serif; font-size: 25px; line-height: 1;
  }
  .detail-label {
    position: absolute; left: 306px;
    font-size: 29px; line-height: 1;
  }
  .detail-label.address { top: 458px; }
  .detail-label.contact { top: 565px; }
</style>
</head>
<body>
  <div class="card">
    <div class="header-left"></div>
    <div class="header-band"></div>
    <div class="divider"></div>
    <div class="side-column"></div>
    <div class="content-panel"></div>

    <div class="brand-name">ORVEL</div>
    <div class="brand-descriptor">Financial Management Pty Ltd</div>

    <svg class="mark-area" viewBox="0 0 255 348" role="img" aria-label="Company mark area">
      <defs>
        <linearGradient id="markTone" x1="0" y1="0" x2="1" y2="1">
          <stop offset="0" stop-color="var(--mark-dark)"/>
          <stop offset="1" stop-color="#3a4244"/>
        </linearGradient>
      </defs>
      <rect x="80" y="95" width="175" height="253" fill="url(#markTone)"/>
    </svg>

    <div class="holder-name">Maren Toll</div>
    <div class="holder-title">FPRB Authorised Financial Strategist</div>

    <div class="detail-label address">Address:-</div>
    <div class="detail-label contact">Contact:-</div>
  </div>
</body>
</html>
```